Business Card for Freelance Copywriting & Web Design Business

Hi! I have a logo but want a new business card. Here's a better idea of what I'm thinking:
-Brand new double-sided business card, rounded cards, embossed logo, nice quality paper
-Include phone (604-382-5194), email (hello@lauraberndt.org), and website (www.lauraberndt.org). No address, please, since I service clients worldwide.
-I'd like the fonts to match those on my website (www.lauraberndt.org). I had to purchase the one font (Born Ready), attached. I'm not sure which version was used on my site so I included all that I purchased. The secondary font is Helvetica
-I'd also like the tagline "Powerful Words. Impressive Results." included.
-My primary brand colour is the teal, colour #19ADC3
Laura Berndt | Laura Berndt Copywriting & Web Design <hello@lauraberndt.org>
-I'd also like the following services listed on the new cards:
SEO Website Content
SEO Blog Content
SEO Website Design
Contact Information for Business Card
as stated in brief
Font styles to use
Other font styles liked:
- See brief
Look and feel
Each slider illustrates characteristics of the customer's brand and the style your logo design should communicate.

```html
<!DOCTYPE html>
<html lang="en">
<head>
<meta charset="utf-8">
<title>Laura Berndt Business Card</title>
<link href="https://fonts.googleapis.com/css2?family=Arimo:wght@400;700&display=swap" rel="stylesheet">
<style>
  :root {
    --backdrop: #2b2b2c;
    --card: #161616;
    --card-edge: #0c0c0c;
    --ink: #ffffff;
    --emboss: #2a2a2a;
    --emboss-light: #3a3a3a;
    --teal: #19adc3;
  }
  * { margin: 0; padding: 0; box-sizing: border-box; }
  html, body {
    width: 1200px;
    height: 689px;
    overflow: hidden;
    background: var(--backdrop);
    font-family: "Arimo", "Helvetica Neue", Helvetica, Arial, sans-serif;
  }
  .canvas {
    position: relative;
    width: 1200px;
    height: 689px;
    display: flex;
    align-items: center;
    justify-content: center;
    gap: 48px;
  }
  .card {
    position: relative;
    width: 540px;
    height: 309px;
    background: var(--card);
    border-radius: 26px;
    box-shadow: 0 2px 0 var(--card-edge), 0 18px 40px rgba(0,0,0,0.45);
    color: var(--ink);
    overflow: hidden;
  }
  .brand-name {
    position: absolute;
    font-weight: 700;
    letter-spacing: 0.5px;
    white-space: nowrap;
  }

  /* Back side */
  .card-back .brand-name {
    top: 92px;
    left: 0;
    width: 100%;
    text-align: center;
    font-size: 46px;
    color: var(--emboss);
    text-shadow: 0 -1px 0 var(--emboss-light);
  }
  .services {
    position: absolute;
    top: 176px;
    left: 0;
    width: 100%;
    text-align: center;
    font-size: 17px;
    line-height: 1.5;
    list-style: none;
  }
  .services li { display: inline; }
  .services li::before { content: "\2022\00a0"; }
  .services li + li { margin-left: 8px; }
  .services .row-break { display: block; margin-left: 0; }

  /* Front side */
  .card-front .brand-name {
    top: 54px;
    left: 0;
    width: 100%;
    text-align: center;
    font-size: 50px;
    color: var(--ink);
  }
  .brand-mark {
    position: absolute;
    top: 134px;
    left: 50%;
    width: 10px;
    height: 10px;
    margin-left: -5px;
    border-radius: 50%;
    background: var(--teal);
  }
  .contact {
    position: absolute;
    top: 168px;
    left: 0;
    width: 100%;
    display: flex;
    justify-content: center;
    gap: 20px;
    font-size: 13px;
    list-style: none;
  }
  .contact li { display: flex; align-items: center; gap: 6px; }
  .contact svg { width: 14px; height: 14px; fill: var(--teal); flex: none; }
  .tagline {
    position: absolute;
    bottom: 44px;
    left: 0;
    width: 100%;
    text-align: center;
    font-size: 24px;
    letter-spacing: 0.3px;
  }
</style>
</head>
<body>
<main class="canvas">

  <section class="card card-back" aria-label="Card back">
    <div class="brand-name">Laura Berndt</div>
    <ul class="services">
      <li>SEO Website Content</li>
      <li>SEO Blog Content</li>
      <li class="row-break">SEO Website Design</li>
    </ul>
  </section>

  <section class="card card-front" aria-label="Card front">
    <div class="brand-name">Laura Berndt</div>
    <span class="brand-mark" aria-hidden="true"></span>
    <ul class="contact">
      <li>
        <svg viewBox="0 0 24 24" aria-hidden="true"><path d="M6.6 10.8a15.1 15.1 0 0 0 6.6 6.6l2.2-2.2a1 1 0 0 1 1-.25 11.4 11.4 0 0 0 3.6.57 1 1 0 0 1 1 1V20a1 1 0 0 1-1 1A17 17 0 0 1 3 4a1 1 0 0 1 1-1h3.5a1 1 0 0 1 1 1c0 1.25.2 2.45.57 3.6a1 1 0 0 1-.25 1z"/></svg>
        (604-382-5194)
      </li>
      <li>
        <svg viewBox="0 0 24 24" aria-hidden="true"><path d="M2 5h20v14H2z M3.5 6.5 12 13l8.5-6.5" /></svg>
        hello@lauraberndt.org
      </li>
      <li>
        <svg viewBox="0 0 24 24" aria-hidden="true"><path d="M12 2a10 10 0 1 0 0 20 10 10 0 0 0 0-20zm6.9 6h-2.9a15 15 0 0 0-1.4-3.6A8 8 0 0 1 18.9 8zM12 4a13 13 0 0 1 1.9 4h-3.8A13 13 0 0 1 12 4zM4.3 14a8 8 0 0 1 0-4h3.4a16 16 0 0 0 0 4zm.8 2h2.9a15 15 0 0 0 1.4 3.6A8 8 0 0 1 5.1 16zM8 8H5.1a8 8 0 0 1 4.3-3.6A15 15 0 0 0 8 8zm4 12a13 13 0 0 1-1.9-4h3.8A13 13 0 0 1 12 20zm2.3-6H9.7a14 14 0 0 1 0-4h4.6a14 14 0 0 1 0 4zm.3 5.6a15 15 0 0 0 1.4-3.6h2.9a8 8 0 0 1-4.3 3.6zm1.7-5.6a16 16 0 0 0 0-4h3.4a8 8 0 0 1 0 4z"/></svg>
        www.lauraberndt.org
      </li>
    </ul>
    <p class="tagline">Powerful Words. Impressive Results</p>
  </section>

</main>
</body>
</html>
```